Herbal Tincture Product Packaging

Rebrand herbal product labels for use on 2 oz tincture bottles - current packaging attached. (no box needed). Bottles are frosted glass Boston rounds 2 oz with silver cap dropper. logo options attached. 3 products/varieties: Harbor, Lantern, Meadow - would really also like a visual icon to represent product variety at a glance, in addition to name.
Please see guidelines below:
Label Material:
Base- polyester, BOPP, or other non-vinyl synthetics Lamination- matte or gloss Backing- white or kraft, no transparent
Spooling:
Rewind direction #4, 3” core, not more that 1200 per roll, not less than 500 per roll Please include 5-10% overage (ex. if you have 500 units on order, please print 525-550 labels).
Sizing:
2oz. ABR- >/= 2” H x 4.5” W
Suggested guidelines review:
https://www.krvl.org/files/Document%20Library/KRVL%20Guidance%20Documents/Packaging%20and%20Labeling/KRVL%20Guidance_Herbal%20Supplements%20Labeling%20Guide%20(Revised%202021).pdf
Target Market(s)
Health Conscious age 24+
Industry/Entity Type
holistic health care
Colors
Look and feel

```html
<!DOCTYPE html>
<html lang="en">
<head>
<meta charset="UTF-8">
<title>Harbor – Herbal Tincture Label</title>
<link rel="stylesheet" href="https://fonts.googleapis.com/css2?family=Arimo:wght@400;700&display=swap">
<style>
  :root {
    --green: #29a04f;
    --purple: #7b2b8b;
    --ink: #1a1a1a;
    --white: #ffffff;
    --leaf-dark: #1a2430;
    --leaf-teal: #1f7f95;
    --leaf-plum: #4a2538;
  }
  * { margin: 0; padding: 0; box-sizing: border-box; }
  html, body { width: 1200px; height: 533px; overflow: hidden; background: var(--white); }
  body { font-family: "Arimo", Arial, sans-serif; }

  .label { position: relative; width: 1200px; height: 533px; background: var(--white); }

  .hero-photo {
    position: absolute; left: 0; top: 0; width: 1200px; height: 251px;
    background:
      radial-gradient(ellipse at 85% 40%, rgba(31,127,149,.75), transparent 45%),
      radial-gradient(ellipse at 20% 70%, rgba(31,127,149,.55), transparent 40%),
      radial-gradient(ellipse at 50% 80%, rgba(74,37,56,.8), transparent 55%),
      linear-gradient(135deg, var(--leaf-dark), var(--leaf-plum) 55%, var(--leaf-dark));
  }

  .brand-tab {
    position: absolute; left: 470px; top: 0; width: 260px; height: 208px;
    background: var(--white); border-radius: 0 0 18px 18px;
    display: flex; flex-direction: column; align-items: center;
  }
  .brand-mark {
    width: 136px; height: 136px; margin-top: 9px;
    border-radius: 50%; background: var(--purple);
  }
  .brand-name {
    margin-top: 12px; font-size: 40px; font-weight: 400; letter-spacing: 10px;
    color: var(--ink); padding-left: 10px; line-height: 1;
  }

  .category-band {
    position: absolute; left: 0; top: 251px; width: 1200px; height: 42px;
    background: var(--green); color: var(--white);
    display: flex; align-items: center; justify-content: center;
    font-size: 21px; font-weight: 400;
  }

  .product-name {
    position: absolute; left: 0; top: 296px; width: 1195px; text-align: center;
    font-size: 68px; font-weight: 700; color: var(--purple); line-height: 1;
  }

  .volume {
    position: absolute; left: 479px; top: 453px;
    font-size: 24px; line-height: 21px; color: var(--ink);
  }
  .volume-rule {
    position: absolute; left: 550px; top: 455px; width: 4px; height: 38px; background: var(--green);
  }
  .descriptor {
    position: absolute; left: 563px; top: 476px;
    font-size: 18px; color: var(--ink); line-height: 1;
  }

  .base-band {
    position: absolute; left: 0; top: 518px; width: 1200px; height: 15px; background: var(--green);
  }
</style>
</head>
<body>
  <main class="label">
    <div class="hero-photo" role="img" aria-label="Close-up photograph of dark teal and plum tropical leaves"></div>

    <div class="brand-tab">
      <div class="brand-mark"></div>
      <div class="brand-name">KOVA</div>
    </div>

    <div class="category-band">LEAS•TONICS•TINCTURES</div>

    <h1 class="product-name">HARBOR</h1>

    <div class="volume">2OZ<br>60ML</div>
    <div class="volume-rule"></div>
    <div class="descriptor">HERBAL SUPPORT</div>

    <div class="base-band"></div>
  </main>
</body>
</html>
```